Large Financial Advisory Firm Needs a Brochure!

We are looking for a modern and professional 4 page brochure for our Financial Advisory firm, Harbrook Counsel Group. I've attached multiple files to help with the completion of the design.
SIZE OF BROCHURE: 17 x 11 FLAT, 8.5 x 11 inch FOLDED
1. A PDF titled Design Brief will provide you with an overview of the project, the text to be included in the brochure and other misc. instructions.
2. Logo Files, you will need to incorporate our logo into the brochure design, I've attached all the files please select the images that suit your design.
3. Competitor Illustration - I've attached an image that needs to be included on the 2nd page (inside left cover of the brochure). You will need to incorporate the pros/cons of using our competitors and the advantages of using our firm. This is outlined in the Design Brief PDF.
NOTE: If possible please get rid of the blue sky in the illustration. Just use the buildings, the blue throws off the concept. I contacted the illustrator and am waiting for a design without the sky but it may not be ready in time so please delete it if possible.
- I like the Avenir fonts, 85 Heavy, 65 Medium and 45.

```html
<!DOCTYPE html>
<html lang="en">
<head>
<meta charset="utf-8">
<title>Harbrook Counsel Group – Brochure Spread</title>
<link rel="stylesheet" href="https://fonts.googleapis.com/css2?family=Nunito+Sans:wght@400;600;800&display=swap">
<style>
  :root {
    --backdrop-light: #e4e4e4;
    --backdrop-dark: #b9b9b9;
    --page-black: #0b0b0b;
    --gold: #e2a81e;
    --gold-deep: #c98f12;
    --body-text: #d6d6d6;
    --tree-grey: #4a4a4a;
  }
  * { box-sizing: border-box; margin: 0; padding: 0; }
  html, body {
    width: 1200px;
    height: 847px;
    overflow: hidden;
  }
  body {
    background: radial-gradient(ellipse at 60% 20%, var(--backdrop-light), var(--backdrop-dark));
    font-family: "Nunito Sans", sans-serif;
    position: relative;
  }
  .spread {
    position: absolute;
    left: 20px;
    top: 48px;
    width: 1160px;
    height: 751px;
    display: flex;
    box-shadow: 0 14px 30px rgba(0,0,0,0.35);
  }
  .page {
    position: relative;
    width: 580px;
    height: 751px;
    background: var(--page-black);
    overflow: hidden;
  }

  /* Back cover */
  .team {
    position: absolute;
    left: 48px;
    top: 52px;
    width: 380px;
    color: var(--body-text);
  }
  .team__title {
    font-weight: 600;
    font-size: 19px;
    color: var(--gold);
    margin-bottom: 20px;
  }
  .member { margin-bottom: 26px; }
  .member__name {
    font-weight: 800;
    font-size: 12.5px;
    color: var(--gold);
    line-height: 1.2;
  }
  .member__role {
    font-weight: 600;
    font-size: 11.5px;
    color: var(--gold);
    margin-bottom: 8px;
  }
  .member__bio {
    font-weight: 400;
    font-size: 9.6px;
    line-height: 1.4;
    margin-bottom: 10px;
  }
  .spine-band {
    position: absolute;
    right: 0;
    top: 0;
    width: 118px;
    height: 100%;
    background: linear-gradient(90deg, var(--gold-deep), var(--gold) 45%, var(--gold-deep));
  }

  /* Front cover */
  .brand {
    position: absolute;
    left: 44px;
    top: 34px;
    display: flex;
    align-items: center;
    gap: 10px;
    color: var(--gold);
    font-weight: 600;
  }
  .brand__mark {
    width: 34px;
    height: 34px;
    background: var(--gold);
  }
  .brand__name { line-height: 1; }
  .brand__primary { display: block; font-size: 27px; letter-spacing: 0.5px; }
  .brand__secondary { display: block; font-size: 9.5px; letter-spacing: 3.2px; margin-top: 2px; }

  .cover-art {
    position: absolute;
    left: 10px;
    top: 90px;
    width: 560px;
    height: 560px;
    background: radial-gradient(circle at 50% 45%, var(--tree-grey) 0%, #2a2a2a 45%, rgba(11,11,11,0) 70%);
  }
  .tagline {
    position: absolute;
    left: 350px;
    top: 500px;
    color: var(--gold);
    font-weight: 600;
    font-size: 18px;
    line-height: 1.2;
    white-space: nowrap;
  }
</style>
</head>
<body>
  <main class="spread">
    <section class="page page--back">
      <div class="team">
        <h2 class="team__title">Our Team</h2>

        <article class="member">
          <h3 class="member__name">Graham Whitlock, CFA, CPA</h3>
          <p class="member__role">Founder</p>
          <p class="member__bio">Graham partners with independent advisors to shape transition plans that protect their clients and their legacy. He pairs fresh thinking with long experience in a field where both are rare. Before starting the firm, he spent years at Westmere Fund Advisors, rising to Regional Director and working with practices across the Pacific Northwest and Mountain states. Time and again he watched trusted advisors search for a successor and come away disappointed, as mismatched values, service models and systems pulled promising agreements apart. Some owners simply stopped looking. Graham created Harbrook Counsel Group so that every advisor can find a successor who fits their practice and their people.</p>
          <p class="member__bio">Graham holds a degree in Economics from Ferncrest University, is a licensed CPA and carries the CFA charter. Away from work he hikes with his wife Marisa, plans trips abroad, practices Italian and Portuguese, and coaches youth soccer.</p>
        </article>

        <article class="member">
          <h3 class="member__name">Owen Hartley, CFA</h3>
          <p class="member__role">Founder</p>
          <p class="member__bio">Owen brings more than a decade of investment management experience to the firm. Earlier in his career he held portfolio management and equity research roles at asset managers and private banks of every size. At Harbrook he oversees investment strategy, guides the operations group and directs the systems work that brings two practices onto one platform. Having taken part in several advisor combinations, he knows first hand where transitions tend to stall and how to keep them moving. Owen was raised in the Pacific Northwest and studied Mathematics and History at Ostermoor College. He is also a CFA charterholder.</p>
          <p class="member__bio">Owen spends his free hours with his wife Clara and their three children. He enjoys rock climbing, woodworking, baking bread and online courses in astronomy.</p>
        </article>

        <article class="member">
          <h3 class="member__name">Miles Hartley</h3>
          <p class="member__role">Founder</p>
          <p class="member__bio">Miles contributes more than a decade of mergers and acquisitions work to the team. His background in valuation, deal terms and business operations lets him tailor each succession plan to the advisor in front of him. Earlier he worked in commercial lending and later launched Crestline Funding, an equipment finance company he led as Chief Executive and grew to more than eighty staff before its sale. Miles studied Philosophy at Halvering University, with a minor in Business Administration.</p>
          <p class="member__bio">Miles and his wife Nora are raising three lively kids. He trains for long distance cycling events, sails on weekends, cooks for friends and treasures time with family.</p>
        </article>
      </div>
      <div class="spine-band"></div>
    </section>

    <section class="page page--front">
      <div class="brand">
        <span class="brand__mark"></span>
        <span class="brand__name">
          <span class="brand__primary">HARBROOK</span>
          <span class="brand__secondary">COUNSEL GROUP</span>
        </span>
      </div>
      <div class="cover-art" role="img" aria-label="Large stylised grey tree emblem with leaf-shaped branches spreading across the cover"></div>
      <p class="tagline">Guiding Every<br>Advisor Transition</p>
    </section>
  </main>
</body>
</html>
```